Billboard design for dentist that sees only children

I own a 12' x 25' digital billboard and I need help with billboard design. My wife is a general dentist that only sees children and is very passionate about giving them a quality dental experience . She has a great reputation in town. Obviously with a billboard there can't be a lot of reading. Maybe something that shows safety, love, experience and children. I am completely open to your ideas. In addition I have other businesses that also need billboard design so this could lead to more work. If you go to Maplecovedental.com under the about section you will find more information about the practice and our phone number. Attached is our logo which could be changed and content specs for the digital billboard. Happy Designing!!

Target Market(s)

Parents with children

Colors

Designer to choose colors to be used in the design.

Requirements
Must have
• Must attract attention and be nice to look at.
Nice to have
• Probably should have children in the picture ..... Maybe
Should not have
• If I see something I don't like I will let you know

```html
<!DOCTYPE html>
<html lang="en">
<head>
<meta charset="utf-8">
<title>Maple Cove Dental – Billboard</title>
<link href="https://fonts.googleapis.com/css2?family=Signika:wght@400&family=Archivo+Black&display=swap" rel="stylesheet">
<style>
  :root {
    --navy: #1b1464;
    --royal: #2b3a92;
    --sky: #0a8fd4;
    --teal-green: #24856b;
    --white: #ffffff;
    --backdrop: #ececf1;
    --photo-warm: #e9b9a0;
    --photo-blue: #6fb7d8;
    --photo-green: #79b34a;
  }
  html, body {
    margin: 0;
    padding: 0;
    width: 1200px;
    height: 840px;
    overflow: hidden;
    background: var(--backdrop);
  }
  .billboard {
    position: absolute;
    left: 0;
    top: 132px;
    width: 1200px;
    height: 575px;
  }
  .billboard svg { display: block; }
  .practice-name {
    font-family: "Signika", "Trebuchet MS", sans-serif;
    font-weight: 400;
    font-size: 84px;
    fill: var(--teal-green);
  }
  .tagline {
    font-family: "Signika", "Trebuchet MS", sans-serif;
    font-style: italic;
    font-size: 34px;
    fill: var(--navy);
  }
  .phone-number {
    font-family: "Archivo Black", "Arial Black", sans-serif;
    font-size: 78px;
    fill: var(--white);
    stroke: var(--navy);
    stroke-width: 9px;
    stroke-linejoin: round;
    paint-order: stroke fill;
    letter-spacing: -2px;
  }
</style>
</head>
<body>
  <main class="billboard">
    <svg width="1200" height="575" viewBox="0 0 1200 575" xmlns="http://www.w3.org/2000/svg">
      <defs>
        <linearGradient id="band-gradient" x1="0" x2="1" y1="0" y2="0">
          <stop offset="0" stop-color="var(--navy)"/>
          <stop offset="0.35" stop-color="var(--sky)"/>
          <stop offset="0.65" stop-color="var(--sky)"/>
          <stop offset="1" stop-color="var(--navy)"/>
        </linearGradient>
        <linearGradient id="photo-gradient" x1="0" x2="1" y1="0" y2="1">
          <stop offset="0" stop-color="var(--photo-warm)"/>
          <stop offset="0.5" stop-color="var(--photo-blue)"/>
          <stop offset="1" stop-color="var(--photo-green)"/>
        </linearGradient>
      </defs>

      <!-- background and top band -->
      <rect class="canvas-white" x="0" y="0" width="1200" height="575" fill="var(--white)"/>
      <rect class="top-band" x="0" y="0" width="1200" height="200" fill="url(#band-gradient)"/>

      <!-- green wave with white field beneath -->
      <path class="wave-stripe"
            d="M0 92 C 150 60, 300 40, 450 70 S 650 140, 740 142 L 1000 165 C 1080 150, 1150 120, 1200 98 L 1200 200 L 0 200 Z"
            fill="var(--teal-green)"/>
      <path class="wave-white"
            d="M0 126 C 150 92, 300 74, 450 102 S 650 170, 740 172 L 1000 195 C 1080 182, 1150 152, 1200 130 L 1200 575 L 0 575 Z"
            fill="var(--white)"/>

      <!-- bottom band -->
      <rect class="bottom-band" x="0" y="520" width="1200" height="55" fill="url(#band-gradient)"/>

      <!-- mark placeholder: plain circle -->
      <circle class="brand-circle" cx="860" cy="192" r="122" fill="var(--white)"/>

      <!-- photo area -->
      <rect class="hero-photo" role="img" aria-label="Photo of four smiling young children leaning together, laughing toward the viewer"
            x="0" y="95" width="480" height="480" rx="60" fill="url(#photo-gradient)" opacity="0.85"/>

      <!-- practice name and tagline -->
      <text class="practice-name" x="1178" y="394" text-anchor="end">Maple Cove Dental</text>
      <text class="tagline" x="1172" y="436" text-anchor="end">general dentistry for children</text>

      <!-- phone -->
      <text class="phone-number" x="842" y="560" text-anchor="middle">555.014.2786</text>
    </svg>
  </main>
</body>
</html>
```